Events and Parties web-site needs a Web Design

VoTrel needs a web design.
VoTrel means The Bees in Italian.
VoTrel target market is people who is organizing parties and events.
Our mission is that the parties and events of our clients exceed their expectations by providing them web and mobile tools.
Our vision is to be the best and biggest party web portal of the country.
The main features of our web site is to let people invite guests and search suppliers/providers. Guests will also confirm presence (RSVP) and buy presents/gifts at the site as well.
Our slogan is "Curta sua festa desde já !" that means "Enjoy our party now !" in Brazilian Portuguese.
The idea here is that the party starts now and not only at the scheduled date and time.
Updates
It seems that must have and nice to have briefing is not appearing to you as I filled. So I will type it agai here:
Our slogan text that is "Curta sua festa desde já !" that means "Enjoy your party now !".
Space to paid ads.
Language switch to Spanish. Brazilian Portuguese is our default language.
Logon form with 2 inputs: Email and password.
RSVP form with 2 inputs: Event ID and password
Kendro trusted site seal (SSL/HTTPS) logo.
Update to my briefing: Only event organizer and guests will be able to see details of the events/parties like photos/blog, guest list and etc. Suppliers will be searched and rated like stayvoro.com/roamgliq.
Target Market(s)
VoTrel target market is amateur and professional people who are organizing parties and events.
Our mission is that the parties and events of our clients exceed their expectations by providing them easy and fast web and mobile tools.
Our vision is to be the best and biggest party portal of our country.
The main features of our web site is to let people invite guests and search suppliers/providers. Guests will also confirm presence (RSVP) and buy presents at the site.
Industry/Entity Type
Events
Requirements
Must have
- Design and colors compliant with attached logo.
- Our slogan text that is "Curta sua festa desde já !" that means "Enjoy your party now !".
- Space to paid ads.
- Language switch to Spanish. Brazilian Portuguese is our default language.
- Logon form with 2 inputs: Email and password.
- RSVP form with 2 inputs: Event ID and password
- Kendro trusted site seal (SSL/HTTPS) logo.
Nice to have
- VoTrel stands for The Bees in Italian. It would be very nice to have a not so explicit idea that each user is a bee and VoTrel is the hive where party/event occurs.
Should not have
- No PageMill please.
- No infant/child oriented designs please. Our market is not only children birthdays but also other parties and events like marriages, corporate events and so on

```html
<!DOCTYPE html>
<html lang="pt-BR">
<head>
<meta charset="utf-8">
<title>VoTrel — Event Planner</title>
<link href="https://fonts.googleapis.com/css2?family=Ubuntu:wght@300;400&family=Lora:ital@0;1&display=swap" rel="stylesheet">
<style>
  :root {
    --cream: #faf7f1;
    --ink: #5a524b;
    --muted: #8d857d;
    --rule: #cfc8bf;
    --brand-dark: #3a1e12;
    --brand-gold: #e7a21c;
    --card: #ffffff;
    --card-soft: rgba(255,255,255,0.92);
    --field: #f4f0ea;
    --icon: #c9c1b6;
  }
  * { margin: 0; padding: 0; box-sizing: border-box; }
  html, body { width: 1200px; height: 776px; overflow: hidden; }
  body { font-family: "Ubuntu", Arial, sans-serif; background: var(--cream); position: relative; }

  /* Sidebar */
  .sidebar { position: absolute; left: 0; top: 0; width: 600px; height: 776px; background: var(--cream); }
  .brand { position: absolute; left: 203px; top: 81px; width: 194px; height: 194px; }
  .brand-ring { position: absolute; inset: 0; }
  .brand-name {
    position: absolute; left: 0; right: 0; top: 108px; text-align: center;
    font-weight: 300; font-size: 31px; color: var(--brand-dark); letter-spacing: 0.5px;
  }
  .tagline {
    position: absolute; left: 0; width: 600px; top: 289px; text-align: center;
    font-weight: 300; font-size: 14px; letter-spacing: 0.6px; color: var(--muted);
  }
  .divider { position: absolute; left: 190px; top: 328px; width: 221px; border-top: 1px solid var(--rule); }

  .main-nav { position: absolute; left: 0; width: 600px; top: 367px; list-style: none; text-align: center; }
  .main-nav li { height: 33.7px; }
  .main-nav a {
    display: inline-block; color: var(--ink); text-decoration: none;
    font-weight: 300; font-size: 15px; letter-spacing: 0.3px;
    padding-bottom: 6px; position: relative;
  }
  .main-nav a::after {
    content: ""; position: absolute; left: 50%; bottom: 0; width: 44px; margin-left: -22px;
    border-bottom: 1px dotted var(--rule);
  }

  .social { position: absolute; left: 213px; top: 646px; width: 174px; height: 58px; border: 1px solid var(--rule);
    display: flex; justify-content: center; align-items: center; gap: 6px; }
  .social a { display: block; width: 22px; height: 22px; border-radius: 50%; background: var(--icon); }
  .copyright {
    position: absolute; left: 0; width: 600px; top: 711px; text-align: center;
    font-weight: 300; font-size: 11.5px; letter-spacing: 0.5px; color: var(--muted);
  }

  /* Hero */
  .hero {
    position: absolute; left: 600px; top: 0; width: 600px; height: 776px;
    background:
      radial-gradient(ellipse 260px 340px at 210px 560px, rgba(214,48,70,0.85), transparent 70%),
      radial-gradient(ellipse 200px 260px at 260px 330px, rgba(160,90,190,0.7), transparent 70%),
      radial-gradient(ellipse 200px 240px at 480px 150px, rgba(60,90,60,0.55), transparent 70%),
      linear-gradient(160deg, #e8c7cd 0%, #d9a3ad 35%, #d4555f 70%, #c8304a 100%);
  }

  .lang-switch { position: absolute; right: 20px; top: 18px; display: flex; gap: 4px; }
  .lang-switch a {
    display: block; padding: 5px 9px; background: var(--card-soft); color: var(--ink);
    font-size: 12px; letter-spacing: 0.6px; text-decoration: none;
  }
  .lang-switch a.is-active { background: var(--brand-dark); color: var(--card); }

  .form-strip {
    position: absolute; left: 755px; width: 445px; height: 50px; background: var(--card-soft);
    display: flex; align-items: center; gap: 8px; padding: 0 12px;
  }
  .form-strip.login { top: 62px; }
  .form-strip.rsvp { top: 120px; }
  .form-label { width: 62px; font-size: 12px; letter-spacing: 0.6px; color: var(--brand-dark); }
  .form-strip input {
    width: 128px; height: 28px; border: 1px solid var(--rule); background: var(--field);
    padding: 0 8px; font-family: "Ubuntu", Arial, sans-serif; font-weight: 300; font-size: 12px; color: var(--ink);
  }
  .form-strip button {
    width: 80px; height: 28px; border: 0; background: var(--brand-gold); color: var(--card);
    font-family: "Ubuntu", Arial, sans-serif; font-size: 12px; letter-spacing: 0.6px;
  }

  .slogan {
    position: absolute; left: 755px; top: 392px; width: 445px;
    font-family: "Lora", Georgia, serif; font-style: italic; font-size: 30px; color: var(--card);
    text-shadow: 0 1px 4px rgba(60,20,20,0.35);
  }

  .event-card {
    position: absolute; left: 755px; top: 446px; width: 445px; height: 66px;
    background: var(--card); display: flex;
  }
  .event-info { flex: 1; padding: 15px 0 0 10px; }
  .event-date { font-family: "Lora", Georgia, serif; font-style: italic; font-size: 13px; color: #9a938c; text-transform: uppercase; }
  .event-title { font-weight: 300; font-size: 21px; color: #3d3833; margin-top: 1px; letter-spacing: 0.2px; }
  .event-next { width: 63px; border-left: 1px solid #dcd6cf; display: flex; align-items: center; justify-content: center; }

  .ad-space {
    position: absolute; left: 755px; top: 590px; width: 445px; height: 96px;
    border: 1px dashed rgba(255,255,255,0.85); background: rgba(255,255,255,0.18);
    display: flex; align-items: center; justify-content: center;
    color: var(--card); font-size: 12px; letter-spacing: 1.2px;
  }
  .trust-seal {
    position: absolute; left: 755px; top: 704px; display: flex; align-items: center; gap: 8px;
    color: var(--card); font-size: 12px; letter-spacing: 0.4px;
  }
  .trust-seal-badge { width: 30px; height: 30px; border-radius: 50%; background: var(--card-soft); }
</style>
</head>
<body>
  <aside class="sidebar">
    <div class="brand">
      <svg class="brand-ring" width="194" height="194" viewBox="0 0 194 194" aria-hidden="true">
        <circle cx="97" cy="97" r="95" fill="none" stroke="#6b625a" stroke-width="1" stroke-dasharray="2 2.5"/>
      </svg>
      <div class="brand-name">VoTrel</div>
    </div>
    <div class="tagline">EVENT PLANNER</div>
    <div class="divider"></div>
    <nav>
      <ul class="main-nav">
        <li><a href="#">ABOUT</a></li>
        <li><a href="#">SERVICES</a></li>
        <li><a href="#">GALLERY</a></li>
        <li><a href="#">BLOG</a></li>
        <li><a href="#">CONTACT</a></li>
      </ul>
    </nav>
    <div class="social">
      <a href="#" aria-label="Social profile 1"></a>
      <a href="#" aria-label="Social profile 2"></a>
      <a href="#" aria-label="Social profile 3"></a>
      <a href="#" aria-label="Social profile 4"></a>
    </div>
    <p class="copyright">COPYRIGHT © 2014 VOTREL</p>
  </aside>

  <div class="hero" role="img" aria-label="Photo of a party table with a painted birthday wine glass, colourful crepe paper streamers and party blowers"></div>

  <nav class="lang-switch" aria-label="Idioma">
    <a href="#" class="is-active">PT</a>
    <a href="#">ES</a>
  </nav>

  <form class="form-strip login" action="#">
    <span class="form-label">ENTRAR</span>
    <input type="email" placeholder="E-mail" aria-label="E-mail">
    <input type="password" placeholder="Senha" aria-label="Senha">
    <button type="submit">OK</button>
  </form>

  <form class="form-strip rsvp" action="#">
    <span class="form-label">RSVP</span>
    <input type="text" placeholder="ID do evento" aria-label="ID do evento">
    <input type="password" placeholder="Senha" aria-label="Senha do evento">
    <button type="submit">CONFIRMAR</button>
  </form>

  <p class="slogan">Curta sua festa desde já !</p>

  <article class="event-card">
    <div class="event-info">
      <div class="event-date">December 25 th, 2013</div>
      <h2 class="event-title">MARLO BIRTHDAY PARTY</h2>
    </div>
    <a class="event-next" href="#" aria-label="Next event">
      <svg width="10" height="18" viewBox="0 0 10 18" aria-hidden="true"><path d="M1 1 L9 9 L1 17" fill="none" stroke="#8d857d" stroke-width="1.4"/></svg>
    </a>
  </article>

  <aside class="ad-space" aria-label="Espaço publicitário">ESPAÇO PUBLICITÁRIO</aside>

  <div class="trust-seal">
    <span class="trust-seal-badge" aria-hidden="true"></span>
    <span>Site seguro Kendro</span>
  </div>
</body>
</html>
```